Company Mission & Values Poster

I'd like an A2 Portrait Poster displaying our company's Mission & Values.
See our website for our logo, fonts, mission & values.
https://talvendo.com.au/

Our Mission: Creating homes for abundant life
Values: Love, Thinking, Team, Zoe.

Some ideas to consider:
Mission as the Headline then
A logo for each of the 4 Values and the words

Target Market(s)

Myself & my team

Industry/Entity Type

Real Estate

Font styles to use
Other font styles liked:
• Company fonts as seen on our website

```html
<!DOCTYPE html>
<html lang="en">
<head>
<meta charset="utf-8">
<title>Talvendo — Mission &amp; Values</title>
<link href="https://fonts.googleapis.com/css2?family=Bodoni+Moda:opsz,wght@6..96,400;6..96,700;6..96,800&family=Young+Serif&display=swap" rel="stylesheet">
<style>
  :root {
    --forest: #05342d;
    --ivory: #ffffff;
    --rule: #c9d6d1;
  }
  * { margin: 0; padding: 0; box-sizing: border-box; }
  html, body { width: 849px; height: 1200px; overflow: hidden; background: var(--forest); }
  .poster {
    position: relative;
    width: 849px;
    height: 1200px;
    background: var(--forest);
    color: var(--ivory);
  }
  .mission {
    position: absolute;
    left: 0; top: 0;
    width: 849px; height: 360px;
  }
  .mission text {
    fill: var(--ivory);
    font-family: "Bodoni Moda", "Didot", serif;
    font-weight: 800;
  }
  .value {
    position: absolute;
    left: 0;
    width: 849px;
    text-align: center;
  }
  .value-title {
    display: flex;
    align-items: center;
    width: 582px;
    margin: 0 auto;
    height: 40px;
  }
  .value-title .rule {
    flex: 1;
    height: 1px;
    background: var(--rule);
  }
  .value-title .dot {
    width: 4px; height: 4px;
    border-radius: 50%;
    background: var(--ivory);
    margin: 0 6px;
  }
  .value-title h2 {
    font-family: "Bodoni Moda", "Didot", serif;
    font-weight: 800;
    font-size: 38px;
    line-height: 40px;
    letter-spacing: 0.5px;
    padding: 0 10px;
  }
  .value-text {
    margin-top: 10px;
    font-family: "Young Serif", Georgia, serif;
    font-size: 14.5px;
    line-height: 27.3px;
    letter-spacing: 0.3px;
  }
  .wordmark {
    position: absolute;
    left: 0; top: 1064px;
    width: 849px;
    text-align: center;
    font-family: "Bodoni Moda", "Didot", serif;
    font-weight: 400;
    font-size: 50px;
    letter-spacing: 9px;
    line-height: 52px;
  }
</style>
</head>
<body>
<main class="poster">
  <svg class="mission" viewBox="0 0 849 360" aria-label="Creating homes for abundant life">
    <text x="138" y="166" font-size="104" textLength="570" lengthAdjust="spacingAndGlyphs">CREATING</text>
    <text x="141" y="292" font-size="142" textLength="567" lengthAdjust="spacingAndGlyphs">HOMES</text>
    <text x="145" y="350" font-size="54" textLength="559" lengthAdjust="spacingAndGlyphs">FOR ABUNDANT LIFE</text>
  </svg>

  <section class="value" style="top:429px">
    <div class="value-title"><span class="rule"></span><span class="dot"></span><h2>LOVE</h2><span class="dot"></span><span class="rule"></span></div>
    <p class="value-text">Our mission is founded in our love and respect for people –<br>those we develop for, those in our teams and those in the<br>communities we create and operate within.</p>
  </section>

  <section class="value" style="top:576px">
    <div class="value-title"><span class="rule"></span><span class="dot"></span><h2>THINKING</h2><span class="dot"></span><span class="rule"></span></div>
    <p class="value-text">We believe in the power of thinking. Our rigorous and creative<br>processes create beautifully considered solutions for our purchasers,<br>the communities we develop within and the environment.</p>
  </section>

  <section class="value" style="top:723px">
    <div class="value-title"><span class="rule"></span><span class="dot"></span><h2>TEAM</h2><span class="dot"></span><span class="rule"></span></div>
    <p class="value-text">Property development is a team sport. We surround ourselves<br>with the best designers and advisers. We strive to create an environment<br>that allows them to do their best work and love doing it.</p>
  </section>

  <section class="value" style="top:872px">
    <div class="value-title"><span class="rule"></span><span class="dot"></span><h2>ZOE</h2><span class="dot"></span><span class="rule"></span></div>
    <p class="value-text">Our mission is to create places for ‘Zoe’<br>the Greek word for abundant life. We do this through exquisite design,<br>quality construction and celebrating nature.</p>
  </section>

  <div class="wordmark">TALVENDO</div>
</main>
</body>
</html>
```